Web and Logo Design - Investing Website

Financial website, so needs to be clean and professional. I like vector images that are simple and professional (data, investing) but do not overpower the website. Will need to show off the charts to emphasize portfolio’s performance. Should be mainly blue and white (does not have to be the blue tones selected). Homepage should have a section where it shows off the three portfolios with a quick summary (see content file) and performance graph (see performance charts file) - with a "learn more" link.

Homepage Header links - Strategies; Monthly Updates; FAQ; Signup; Login

Pages needed:
Homepage
Articles/Blog Main Page
Article Layout Template
Dashboard Template (see Dashboard information file)

Sample designs i like: https://www.plimvaro.io/ - https://www.brastekin.com/ - https://www.holvendarquist.com/

Industry/Entity Type

Finance - Investing

Number of Pages Required

4 page

Colors
0054AA
0677BA
7BADD7
CADEEF
E8F1F8

Requirements
Should not have
• Generic pictures of people

```html
<!DOCTYPE html>
<html lang="en">
<head>
<meta charset="utf-8">
<title>Quantrail Capital</title>
<link href="https://fonts.googleapis.com/css2?family=Open+Sans:wght@400;600;700;800&family=Roboto:wght@400;500;700&display=swap" rel="stylesheet">
<style>
:root{
  --brand:#1a7cc4;
  --deep:#0b3f94;
  --sky:#2fb4e0;
  --ink:#1f2a36;
  --text:#4a4f55;
  --pale:#d9ecf8;
  --bar-blue:#7f9cf0;
  --bar-red:#e46a6a;
  --grid:#e3e6ea;
  --white:#ffffff;
}
*{box-sizing:border-box;margin:0;padding:0}
html,body{width:1200px;height:3306px;overflow:hidden;background:var(--white)}
body{position:relative;font-family:"Open Sans",sans-serif;color:var(--text)}
.abs{position:absolute}
/* header */
.brand{left:110px;top:31px;font:600 25px "Open Sans",sans-serif;color:var(--ink)}
.nav{left:557px;top:40px;font:500 14.5px "Roboto",sans-serif;color:var(--ink)}
.nav a{position:absolute;white-space:nowrap;color:var(--ink);text-decoration:none}
.nav a.active::after{content:"";position:absolute;left:0;right:0;top:22px;height:3px;background:var(--brand)}
.hero-art{left:92px;top:109px;width:537px;height:533px;border-radius:40px;background:radial-gradient(circle at 50% 50%,#e6f2fb,#cfe3f6 60%,#ffffff 100%)}
.hero-blob{left:626px;top:132px}
.hero-title{left:699px;top:254px;width:420px;font:800 35px/41px "Open Sans",sans-serif;color:var(--white);letter-spacing:.3px}
.btn-start{left:697px;top:432px;width:148px;height:45px;border-radius:23px;background:var(--white);color:var(--brand);font:700 14px/45px "Open Sans",sans-serif;text-align:center}
.dots{left:713px;top:625px;display:flex;gap:5px}
.dots span{width:11px;height:11px;border-radius:50%;background:#c9ccd0}
.dots span.on{background:var(--brand)}
/* about */
.about{left:0;top:685px;width:1200px;height:375px;background:linear-gradient(90deg,var(--deep),#1570bd 55%,var(--sky))}
.about-wave{left:0;top:990px}
.about h2{position:absolute;top:96px;width:1200px;text-align:center;font:700 36px "Open Sans",sans-serif;color:var(--white)}
.about p{position:absolute;left:300px;top:147px;width:600px;text-align:center;font:400 14px/25.7px "Open Sans",sans-serif;color:var(--white)}
/* portfolios */
.section-title{left:0;width:1200px;text-align:center;font:800 37px "Open Sans",sans-serif;color:var(--ink)}
.disc{border-radius:50%;background:var(--brand)}
.chart-card{background:var(--white);box-shadow:0 4px 14px rgba(0,0,0,.18)}
.pf-icon{width:78px;height:78px;border-radius:50%;background:var(--pale)}
.pf-title{font:700 26px "Open Sans",sans-serif;color:var(--ink);letter-spacing:.5px;white-space:nowrap}
.pf-text{font:400 14.6px/22.5px "Open Sans",sans-serif;color:var(--text)}
.right{text-align:right}
/* included */
.included{left:0;top:2503px;width:1200px;height:400px;background:linear-gradient(180deg,var(--sky),#1470bb 55%,var(--deep))}
.included h2{position:absolute;top:78px;width:1200px;text-align:center;font:700 36px "Open Sans",sans-serif;color:var(--white)}
.perk{position:absolute;top:141px;width:220px;text-align:center}
.perk-badge{width:120px;height:120px;margin:0 auto;background:var(--white);border-radius:50% 50% 50% 14%;display:flex;align-items:center;justify-content:center}
.perk-label{margin-top:22px;font:700 19.5px/23px "Open Sans",sans-serif;color:var(--white)}
/* footer */
.f-col{top:2986px}
.f-col h4{font:700 13.5px "Roboto",sans-serif;color:var(--ink);margin-bottom:16px}
.f-col li{list-style:none;font:400 14.5px "Roboto",sans-serif;color:var(--text);height:37px;display:flex;align-items:center;gap:14px}
.chev{font-size:13px;color:var(--ink)}
.social{display:flex;gap:10px;margin-top:4px}
.social span{width:31px;height:31px;border-radius:50%;border:2px solid var(--ink)}
.subscribe{margin-top:28px;font:700 13.5px "Roboto",sans-serif;color:var(--ink);text-decoration:underline}
.email{margin-top:18px;width:311px;height:47px;border:1px solid #d5d9de;box-shadow:0 2px 6px rgba(0,0,0,.12);display:flex;align-items:center;justify-content:space-between;font:400 14.5px "Roboto",sans-serif;color:var(--text);padding-left:17px}
.email b{width:48px;height:47px;background:var(--brand);display:flex;align-items:center;justify-content:center}
.copy{left:0;top:3259px;width:1200px;text-align:center;font:400 14px "Roboto",sans-serif;color:var(--ink)}
svg text{font-family:"Roboto",sans-serif}
</style>
</head>
<body>

<header>
  <div class="abs brand">Quantrail Capital</div>
  <nav class="abs nav">
    <a class="active" style="left:0">HOME</a>
    <a style="left:76px">ABOUT US</a>
    <a style="left:180px">SERVICES</a>
    <a style="left:276px">BLOG</a>
    <a style="left:346px">REVIEWS</a>
    <a style="left:439px">CONTACT US</a>
  </nav>
</header>

<section class="hero">
  <div class="abs hero-art" role="img" aria-label="Isometric illustration of a desktop computer and laptop showing data charts, with a magnifying glass over a report"></div>
  <svg class="abs hero-blob" width="546" height="478" viewBox="0 0 546 478" aria-hidden="true">
    <path d="M70 70 C150 -10 400 -15 490 70 C570 150 555 320 430 410 C310 495 120 470 45 360 C-10 275 0 140 70 70 Z" fill="var(--brand)"/>
  </svg>
  <h1 class="abs hero-title">RULES-BASED INVESTING STRATEGIES USING QUANTITATIVE ANALYSIS</h1>
  <div class="abs btn-start">GET STARTED</div>
  <div class="abs dots"><span class="on"></span><span></span><span></span></div>
</section>

<section class="abs about">
  <h2>ABOUT US</h2>
  <p>QuantrailCapital.com uses market data, factoring and backtesting to make data driven investment decisions and help craft portfolios that have a high probability of beating the market over the long term. Our algorithms provide rules based investment strategies that investors trade in their own accounts.</p>
</section>
<svg class="abs about-wave" width="1200" height="72" viewBox="0 0 1200 72" aria-hidden="true">
  <path d="M0 30 C250 66 600 62 1200 4 L1200 72 L0 72 Z" fill="var(--white)"/>
</svg>

<h2 class="abs section-title" style="top:1130px">OUR PORTFOLIOS</h2>

<!-- Conservative -->
<div class="abs disc" style="left:187px;top:1210px;width:340px;height:340px"></div>
<div class="abs chart-card" style="left:139px;top:1262px;width:435px;height:237px">
  <svg width="435" height="237" viewBox="0 0 435 237">
    <text x="217" y="16" font-size="11" text-anchor="middle" fill="#444">Conservative ETF Rotation</text>
    <g stroke="var(--grid)" stroke-width="1">
      <line x1="60" x2="425" y1="30" y2="30"/><line x1="60" x2="425" y1="48" y2="48"/><line x1="60" x2="425" y1="66" y2="66"/><line x1="60" x2="425" y1="84" y2="84"/><line x1="60" x2="425" y1="103" y2="103"/><line x1="60" x2="425" y1="121" y2="121"/><line x1="60" x2="425" y1="139" y2="139"/><line x1="60" x2="425" y1="157" y2="157"/><line x1="60" x2="425" y1="175" y2="175"/>
    </g>
    <g font-size="7" fill="#666" text-anchor="end">
      <text x="55" y="32">160.00%</text><text x="55" y="50">140.00%</text><text x="55" y="68">120.00%</text><text x="55" y="86">100.00%</text><text x="55" y="105">80.00%</text><text x="55" y="123">60.00%</text><text x="55" y="141">40.00%</text><text x="55" y="159">20.00%</text><text x="55" y="177">0.00%</text>
    </g>
    <g fill="var(--bar-blue)"><rect x="76" y="155.5" width="28" height="19.5"/><rect x="167" y="148.8" width="28" height="26.2"/><rect x="258" y="90.4" width="28" height="84.6"/><rect x="350" y="53" width="28" height="122"/></g>
    <g fill="var(--bar-red)"><rect x="106" y="170.9" width="28" height="4.1"/><rect x="197" y="168.3" width="28" height="6.7"/><rect x="288" y="145.1" width="28" height="29.9"/><rect x="380" y="125.9" width="28" height="49.1"/></g>
    <g font-size="7" fill="#555" text-anchor="middle">
      <text x="90" y="151">21.56%</text><text x="120" y="167">4.49%</text><text x="181" y="145">28.90%</text><text x="211" y="164">7.43%</text><text x="272" y="87">93.38%</text><text x="302" y="141">33.05%</text><text x="364" y="49">134.62%</text><text x="394" y="122">54.20%</text>
      <text x="105" y="190">YTD Return</text><text x="196" y="190">1yr Return</text><text x="287" y="190">3yr Return</text><text x="379" y="190">5yr Return</text>
    </g>
    <g font-size="7" fill="#555"><rect x="135" y="217" width="5" height="5" fill="var(--bar-blue)"/><text x="142" y="222">Quant 60/40</text><rect x="196" y="217" width="5" height="5" fill="var(--bar-red)"/><text x="203" y="222">All World 60/40 (Benchmark)</text></g>
  </svg>
</div>
<div class="abs pf-icon" style="left:599px;top:1245px" role="img" aria-label="Icon of two hands holding a growing plant"></div>
<h3 class="abs pf-title" style="left:599px;top:1340px">CONSERVATIVE ETF ROTATION</h3>
<p class="abs pf-text" style="left:599px;top:1392px;width:490px">Holds 2 ETFs and are rotated and/or rebalanced on the last trading day of the month. Holds a 60% Equity and 40% Bond allocation. It switches its equity allocation to cash when volatility comes into the market. It is backtested to beat a 60/40 portfolio and keep up with the Broad Market Index with less drawdowns and volatility.</p>

<!-- Growth -->
<div class="abs disc" style="left:674px;top:1622px;width:340px;height:340px"></div>
<div class="abs chart-card" style="left:628px;top:1675px;width:432px;height:236px">
  <svg width="432" height="236" viewBox="0 0 432 236">
    <text x="14" y="18" font-size="11" fill="#444">Growth ETF Rotation</text>
    <g stroke="var(--grid)" stroke-width="1">
      <line x1="60" x2="425" y1="30" y2="30"/><line x1="60" x2="425" y1="54" y2="54"/><line x1="60" x2="425" y1="78" y2="78"/><line x1="60" x2="425" y1="103" y2="103"/><line x1="60" x2="425" y1="127" y2="127"/><line x1="60" x2="425" y1="151" y2="151"/><line x1="60" x2="425" y1="175" y2="175"/>
    </g>
    <g font-size="7" fill="#666" text-anchor="end">
      <text x="55" y="32">300.00%</text><text x="55" y="56">250.00%</text><text x="55" y="80">200.00%</text><text x="55" y="105">150.00%</text><text x="55" y="129">100.00%</text><text x="55" y="153">50.00%</text><text x="55" y="177">0.00%</text>
    </g>
    <g fill="var(--bar-blue)"><rect x="76" y="164.6" width="28" height="10.4"/><rect x="167" y="158.9" width="28" height="16.1"/><rect x="258" y="111" width="28" height="64"/><rect x="350" y="37.3" width="28" height="137.7"/></g>
    <g fill="var(--bar-red)"><rect x="106" y="167.3" width="28" height="7.7"/><rect x="197" y="162.9" width="28" height="12.1"/><rect x="288" y="147.6" width="28" height="27.4"/><rect x="380" y="118.2" width="28" height="56.8"/></g>
    <g font-size="7" fill="#555" text-anchor="middle">
      <text x="90" y="160">21.42%</text><text x="120" y="163">15.92%</text><text x="181" y="154">33.33%</text><text x="211" y="158">25.12%</text><text x="272" y="107">132.37%</text><text x="302" y="143">56.66%</text><text x="364" y="33">284.95%</text><text x="394" y="114">117.49%</text>
      <text x="105" y="190">YTD Return</text><text x="196" y="190">1yr Return</text><text x="287" y="190">3yr Return</text><text x="379" y="190">5yr Return</text>
    </g>
    <g font-size="7" fill="#555"><rect x="172" y="217" width="5" height="5" fill="var(--bar-blue)"/><text x="179" y="222">Quant Rotation</text><rect x="227" y="217" width="5" height="5" fill="var(--bar-red)"/><text x="234" y="222">Market Benchmark</text></g>
  </svg>
</div>
<div class="abs pf-icon" style="left:522px;top:1655px" role="img" aria-label="Icon of a rising bar chart with an upward arrow"></div>
<h3 class="abs pf-title right" style="left:202px;top:1751px;width:400px">GROWTH ETF ROTATION</h3>
<p class="abs pf-text right" style="left:108px;top:1802px;width:494px">Holds 4 ETFs and are rotated and/or rebalanced on the last trading day of the month. The strategy holds the strongest sectors. The allocation will sometimes be a full equity allocation, and sometimes have a bond allocation. This strategy is back-tested to beat the market long term with less volatility.</p>

<!-- Whale -->
<div class="abs disc" style="left:187px;top:2059px;width:340px;height:340px"></div>
<div class="abs chart-card" style="left:136px;top:2109px;width:442px;height:242px">
  <svg width="442" height="242" viewBox="0 0 442 242">
    <text x="221" y="16" font-size="11" text-anchor="middle" fill="#444">Whale Rotation</text>
    <g stroke="var(--grid)" stroke-width="1">
      <line x1="60" x2="430" y1="30" y2="30"/><line x1="60" x2="430" y1="46" y2="46"/><line x1="60" x2="430" y1="62" y2="62"/><line x1="60" x2="430" y1="78" y2="78"/><line x1="60" x2="430" y1="94" y2="94"/><line x1="60" x2="430" y1="111" y2="111"/><line x1="60" x2="430" y1="127" y2="127"/><line x1="60" x2="430" y1="143" y2="143"/><line x1="60" x2="430" y1="159" y2="159"/><line x1="60" x2="430" y1="175" y2="175"/>
    </g>
    <g font-size="7" fill="#666" text-anchor="end">
      <text x="55" y="32">180.00%</text><text x="55" y="48">160.00%</text><text x="55" y="64">140.00%</text><text x="55" y="80">120.00%</text><text x="55" y="96">100.00%</text><text x="55" y="113">80.00%</text><text x="55" y="129">60.00%</text><text x="55" y="145">40.00%</text><text x="55" y="161">20.00%</text><text x="55" y="177">0.00%</text>
    </g>
    <g fill="var(--bar-blue)"><rect x="76" y="167.2" width="28" height="7.8"/><rect x="167" y="148.8" width="28" height="26.2"/><rect x="258" y="115.3" width="28" height="59.7"/><rect x="350" y="51.1" width="28" height="123.9"/></g>
    <g fill="var(--bar-red)"><rect x="106" y="165" width="28" height="10"/><rect x="197" y="142.9" width="28" height="32.1"/><rect x="288" y="124.6" width="28" height="50.4"/><rect x="380" y="79.4" width="28" height="95.6"/></g>
    <g font-size="7" fill="#555" text-anchor="middle">
      <text x="90" y="163">9.68%</text><text x="120" y="161">12.38%</text><text x="181" y="145">32.50%</text><text x="211" y="139">39.85%</text><text x="272" y="111">74.09%</text><text x="302" y="121">62.52%</text><text x="364" y="47">153.75%</text><text x="394" y="75">118.61%</text>
      <text x="105" y="190">YTD Return</text><text x="196" y="190">1yr Return</text><text x="287" y="190">3yr Return</text><text x="379" y="190">5yr Return</text>
    </g>
    <g font-size="7" fill="#555"><rect x="168" y="222" width="5" height="5" fill="var(--bar-blue)"/><text x="175" y="227">Whale Rotation</text><rect x="223" y="222" width="5" height="5" fill="var(--bar-red)"/><text x="230" y="227">Broad Market Index</text></g>
  </svg>
</div>
<div class="abs pf-icon" style="left:599px;top:2094px" role="img" aria-label="Icon of a whale tail above waves"></div>
<h3 class="abs pf-title" style="left:599px;top:2188px">WHALE ROTATION</h3>
<p class="abs pf-text" style="left:599px;top:2240px;width:494px">Holds 4 large cap stocks and are rotated and/or rebalanced on the last trading day of the month. This will always have a 100% equity allocation, so the volatility and drawdowns will be larger. This strategy has shown to beat the market significantly over the mid to long term.</p>

<section class="abs included">
  <h2>WHAT'S INCLUDED</h2>
  <div class="perk" style="left:122px">
    <div class="perk-badge"><svg width="62" height="62" viewBox="0 0 62 62" fill="none" stroke="var(--brand)" stroke-width="2.5" stroke-linejoin="round"><rect x="6" y="18" width="50" height="34" rx="3"/><path d="M12 18 L40 8 L44 18"/><rect x="36" y="30" width="20" height="10" rx="2"/><circle cx="42" cy="35" r="2"/></svg></div>
    <div class="perk-label">Updates to all<br>portfolios</div>
  </div>
  <div class="perk" style="left:367px">
    <div class="perk-badge"><svg width="62" height="62" viewBox="0 0 62 62" fill="none" stroke="var(--brand)" stroke-width="2.5" stroke-linejoin="round"><line x1="31" y1="6" x2="31" y2="52"/><path d="M31 12 H48 L54 18 L48 24 H31"/><path d="M31 28 H14 L8 34 L14 40 H31"/><path d="M10 54 H52"/></svg></div>
    <div class="perk-label">14 day free trial</div>
  </div>
  <div class="perk" style="left:611px">
    <div class="perk-badge"><svg width="62" height="62" viewBox="0 0 62 62" fill="none" stroke="var(--brand)" stroke-width="2.5" stroke-linecap="round"><circle cx="31" cy="31" r="22"/><path d="M23 23 L39 39 M39 23 L23 39"/></svg></div>
    <div class="perk-label">Cancel anytime</div>
  </div>
  <div class="perk" style="left:858px">
    <div class="perk-badge"><svg width="62" height="62" viewBox="0 0 62 62" fill="none" stroke="var(--brand)" stroke-width="2.5" stroke-linejoin="round"><path d="M34 8 H54 V30 L32 52 L12 32 Z"/><circle cx="46" cy="16" r="3"/><text x="28" y="38" font-size="16" fill="var(--brand)" stroke="none" font-family="Roboto,sans-serif" font-weight="700">$</text></svg></div>
    <div class="perk-label">Price<br>.$14.95/M</div>
  </div>
</section>

<footer>
  <div class="abs f-col" style="left:110px">
    <h4>QUICK LINKS</h4>
    <ul><li><span class="chev">»</span>Home</li><li><span class="chev">»</span>About Us</li><li><span class="chev">»</span>Our Products</li><li><span class="chev">»</span>Reviews</li><li><span class="chev">»</span>Latest Blog</li></ul>
  </div>
  <div class="abs f-col" style="left:295px">
    <h4>OTHER LINKS</h4>
    <ul><li><span class="chev">»</span>Terms &amp; Conditions</li><li><span class="chev">»</span>Privacy Policy</li><li><span class="chev">»</span>Help Service</li><li><span class="chev">»</span>FAQ</li><li><span class="chev">»</span>Contact us</li></ul>
  </div>
  <div class="abs f-col" style="left:526px">
    <h4>FIND US ON</h4>
    <ul>
      <li><svg width="12" height="14" viewBox="0 0 12 14"><path d="M6 0 A5 5 0 0 1 11 5 C11 9 6 14 6 14 C6 14 1 9 1 5 A5 5 0 0 1 6 0 Z" fill="var(--ink)"/><circle cx="6" cy="5" r="2" fill="#fff"/></svg>&nbsp;&nbsp;418, Wrenfield Avenue</li>
      <li style="padding-left:31px">United States</li>
      <li><svg width="13" height="13" viewBox="0 0 13 13"><path d="M2 1 L5 1 L6 4 L4 5.5 C5 8 6 9 8 9.5 L9.5 7.5 L12.5 8.5 L12.5 11.5 C7 12.5 0.5 6 2 1 Z" fill="var(--ink)"/></svg>&nbsp;&nbsp;1 555 014 2276</li>
      <li><svg width="14" height="11" viewBox="0 0 14 11" fill="none" stroke="var(--ink)" stroke-width="1.4"><rect x="1" y="1" width="12" height="9"/><path d="M1 1 L7 6 L13 1"/></svg>&nbsp;&nbsp;info@quantrailmail.com</li>
    </ul>
  </div>
  <div class="abs f-col" style="left:779px">
    <h4>CONNECTED US ON</h4>
    <div class="social"><span></span><span></span><span></span><span></span><span></span></div>
    <div class="subscribe">SUBSCRIBE TO OUR NEWSLETTER</div>
    <div class="email">Email Address<b><svg width="20" height="20" viewBox="0 0 20 20"><path d="M19 1 L1 9 L9 11 L11 19 Z" fill="#fff"/></svg></b></div>
  </div>
  <div class="abs copy">© 2021 Company name. All Rights Reserved</div>
</footer>

</body>
</html>
```